Pheasant Farm needs a logo design

I need a logo design for my Pheasant farm. We raise Pheasants from chicks to adult birds for the hunting clubs dog training and restocking. I would like a logo that makes it easy to see that we deal with Pheasants. My company name is Larkin Meadow Pines located in northern MN. I'd like a pheasant in the logo if possible.

Target Market(s)

Hunting clubs, dog trainers, hunters

Contact Information for Business Card

Larkin Meadow Pines Dale Wexby cell 715-463-2098 office 218-302-7746 tallgrassfowlyard.com tallgrassfowlyard@quailpostmail.com
5816 Bramwell Rd NE
Birchmoor, WI 56519

```html
<!DOCTYPE html>
<html lang="en">
<head>
<meta charset="utf-8">
<title>Larkin Meadow Pines – Business Card</title>
<link href="https://fonts.googleapis.com/css2?family=Libre+Baskerville:wght@400;700&display=swap" rel="stylesheet">
<style>
  :root {
    --backdrop: #bba6a6;
    --card-light: #ffffff;
    --card-shade: #e7e7ea;
    --brand-brown: #7a5a3e;
    --ink: #161616;
  }
  html, body {
    margin: 0;
    padding: 0;
    width: 1200px;
    height: 1200px;
    overflow: hidden;
    background: var(--backdrop);
    font-family: "Libre Baskerville", "Palatino Linotype", serif;
  }
  .canvas {
    position: relative;
    width: 1200px;
    height: 1200px;
  }
  .card {
    position: absolute;
    left: 250px;
    width: 700px;
    height: 400px;
    background: linear-gradient(135deg, var(--card-light) 20%, var(--card-shade) 100%);
  }
  .card--front { top: 147px; }
  .card--back { top: 652px; }

  .brand {
    position: absolute;
    display: flex;
    align-items: center;
    gap: 12px;
    color: var(--brand-brown);
    font-weight: 400;
    white-space: nowrap;
    transform: translate(-50%, -50%);
  }
  .brand__dot {
    border: 2px solid var(--brand-brown);
    border-radius: 50%;
    flex: none;
  }
  .card--front .brand { left: 350px; top: 200px; font-size: 30px; letter-spacing: 0.06em; }
  .card--front .brand__dot { width: 18px; height: 18px; }
  .card--back .brand { left: 560px; top: 95px; font-size: 15px; letter-spacing: 0.06em; gap: 8px; }
  .card--back .brand__dot { width: 10px; height: 10px; }

  .holder-name {
    position: absolute;
    left: 37px;
    top: 194px;
    margin: 0;
    font-size: 27px;
    font-weight: 700;
    color: var(--brand-brown);
    letter-spacing: 0.01em;
  }
  .divider {
    position: absolute;
    left: 0;
    top: 236px;
    width: 100%;
    height: 3px;
    background: var(--brand-brown);
  }
  .contact-list {
    position: absolute;
    top: 0;
    margin: 0;
    padding: 0;
    list-style: none;
    color: var(--ink);
    font-size: 16px;
  }
  .contact-list--left { left: 36px; }
  .contact-list--right { left: 342px; }
  .contact-item {
    position: absolute;
    left: 0;
    display: flex;
    align-items: center;
    white-space: nowrap;
    transform: translateY(-50%);
  }
  .contact-item svg {
    width: 26px;
    height: 22px;
    flex: none;
    margin-right: 16px;
    fill: var(--ink);
  }
  .contact-item--plain { padding-left: 42px; }
  .contact-item--email { font-size: 14px; }
</style>
</head>
<body>
<main class="canvas">

  <section class="card card--front" aria-label="Card front">
    <div class="brand">
      <span class="brand__dot"></span>
      <span class="brand__name">Larkin Meadow Pines</span>
    </div>
  </section>

  <section class="card card--back" aria-label="Card back">
    <div class="brand">
      <span class="brand__dot"></span>
      <span class="brand__name">Larkin Meadow Pines</span>
    </div>

    <h1 class="holder-name">DALE WEXBY</h1>
    <div class="divider"></div>

    <ul class="contact-list contact-list--left">
      <li class="contact-item" style="top:286px">
        <svg viewBox="0 0 24 24" aria-hidden="true"><path d="M6.6 10.8c1.4 2.8 3.8 5.1 6.6 6.6l2.2-2.2c.3-.3.7-.4 1-.2 1.1.4 2.3.6 3.6.6.6 0 1 .4 1 1V20c0 .6-.4 1-1 1C10.6 21 3 13.4 3 4c0-.6.4-1 1-1h3.5c.6 0 1 .4 1 1 0 1.3.2 2.5.6 3.6.1.3 0 .7-.2 1z"/></svg>
        <span>715-463-2098</span>
      </li>
      <li class="contact-item" style="top:322px">
        <svg viewBox="0 0 24 24" aria-hidden="true"><rect x="2" y="3" width="5" height="18" rx="1"/><path d="M9 7h13v14H9z"/><rect x="11" y="3" width="8" height="3"/><g fill="#fff"><rect x="11" y="10" width="2" height="2"/><rect x="14.5" y="10" width="2" height="2"/><rect x="18" y="10" width="2" height="2"/><rect x="11" y="14" width="2" height="2"/><rect x="14.5" y="14" width="2" height="2"/><rect x="18" y="14" width="2" height="2"/></g></svg>
        <span>218-302-7746</span>
      </li>
      <li class="contact-item" style="top:356px">
        <svg viewBox="0 0 24 24" aria-hidden="true"><path fill="none" stroke="#161616" stroke-width="1.5" d="M12 2a10 10 0 1 0 0 20a10 10 0 1 0 0-20zM2 12h20M12 2c-3 3-3 17 0 20M12 2c3 3 3 17 0 20M4 6.5h16M4 17.5h16"/><path d="M14 13l8 3-3.5 1.2L17 21z"/></svg>
        <span>tallgrassfowlyard.com</span>
      </li>
    </ul>

    <ul class="contact-list contact-list--right">
      <li class="contact-item contact-item--email" style="top:287px">
        <svg viewBox="0 0 26 18" aria-hidden="true"><path d="M0 0h26v18H0z"/><path d="M1 1l12 9 12-9M1 17l9-8M25 17l-9-8" fill="none" stroke="#fff" stroke-width="1.4"/></svg>
        <span>tallgrassfowlyard@quailpostmail.com</span>
      </li>
      <li class="contact-item" style="top:321px">
        <svg viewBox="0 0 24 24" aria-hidden="true"><path d="M12 1a7 7 0 0 0-7 7c0 5 7 12 7 12s7-7 7-12a7 7 0 0 0-7-7zm0 9.5a2.5 2.5 0 1 1 0-5a2.5 2.5 0 0 1 0 5z"/><ellipse cx="12" cy="22" rx="5" ry="1.3"/></svg>
        <span>5816 Bramwell Rd NE</span>
      </li>
      <li class="contact-item contact-item--plain" style="top:355px">
        <span>Birchmoor, WI 56519</span>
      </li>
    </ul>
  </section>

</main>
</body>
</html>
```